Rural contractor needs professional informative business card

We need a business card design that looks professional but also includes information about the services that the business offers.
The business is an earthmoving and transport business. All of the services offered are listed on the old card attached.
The business is aimed at farmers so the design we are after is a classic look. The card needs to include all of the information that is listed on the old card design uploaded as an attachment. We recognize that this is a lot of information to fit on a business card but it also operates as a key marketing tool so is very important to the business.
Feel free to send me your questions.
Thanks
Reason: We are having trouble deciding between all these great designs - thank you for your efforts
We would love to see some designs using red with a little white and black. Also feel free to re-design our logo if you feel it needs to be to fit your designs. Thank you

```html
<!DOCTYPE html>
<html lang="en">
<head>
<meta charset="utf-8">
<title>BK Harlowe Contracting – Business Card</title>
<link href="https://fonts.googleapis.com/css2?family=Roboto+Condensed:wght@400;700&display=swap" rel="stylesheet">
<style>
  :root {
    --stage: #f1f3f4;
    --soil-dark: #2e2824;
    --soil-mid: #4a403a;
    --brand-red: #b3121b;
    --deep-red: #7d0b10;
    --bright-red: #d3161f;
    --ink: #141111;
    --white: #ffffff;
  }
  * { margin: 0; padding: 0; box-sizing: border-box; }
  html, body { width: 1200px; height: 686px; overflow: hidden; }
  body {
    background: radial-gradient(ellipse at center, #fbfbfb 0%, var(--stage) 70%, #e6e8e9 100%);
    font-family: "Roboto Condensed", "Arial Narrow", sans-serif;
    position: relative;
  }
  .card { position: absolute; overflow: hidden; }

  /* Front */
  .card-front { left: 47px; top: 68px; width: 535px; height: 305px; }
  .soil {
    position: absolute; inset: 0;
    background: radial-gradient(ellipse at 50% 40%, var(--soil-mid) 0%, var(--soil-dark) 75%);
  }
  .front-name {
    position: absolute; left: 0; right: 0; top: 70px;
    text-align: center; color: var(--brand-red); font-weight: 700;
  }
  .front-name .name-main { display: block; font-size: 64px; line-height: 64px; letter-spacing: -1px; }
  .front-name .name-sub { display: block; font-size: 22px; letter-spacing: 12px; margin-top: 14px; padding-left: 12px; }
  .contact {
    position: absolute; color: var(--white); font-size: 13px; letter-spacing: 0.6px;
    display: flex; align-items: center; gap: 6px;
  }
  .contact svg { width: 12px; height: 12px; fill: var(--bright-red); }
  .contact-email { left: 32px; top: 234px; }
  .contact-email svg { order: -1; }
  .contact-phone { right: 24px; top: 216px; }
  .contact-address { right: 24px; top: 235px; }
  .tagline {
    position: absolute; left: 0; right: 0; bottom: 0; height: 38px;
    background: linear-gradient(180deg, var(--bright-red), var(--deep-red));
    color: var(--white); font-weight: 700; font-size: 22px;
    text-align: center; line-height: 38px;
  }

  /* Back */
  .card-back { left: 616px; top: 297px; width: 537px; height: 304px; background: var(--brand-red); }
  .back-soil { position: absolute; left: 0; top: 0; width: 187px; height: 304px;
    background: radial-gradient(ellipse at 50% 30%, var(--soil-mid), var(--soil-dark)); }
  .divider { position: absolute; left: 187px; top: 0; width: 19px; height: 304px; background: var(--ink);
    border-left: 2px solid var(--deep-red); }
  .divider::after { content: ""; position: absolute; left: 7px; top: 0; width: 2px; height: 100%; background: var(--bright-red); }
  .machinery-photo { position: absolute; left: 206px; top: 0; right: 0; bottom: 0;
    background: linear-gradient(135deg, var(--bright-red) 0%, #a51018 55%, #8d0d13 100%); }
  .truck-photo { position: absolute; left: 0; top: 138px; width: 254px; height: 166px;
    background: linear-gradient(180deg, #e9ecef 0%, #c9ced3 60%, #3a3535 100%);
    border-top-right-radius: 30px 10px; }
  .back-name {
    position: absolute; left: 21px; top: 21px; width: 148px; height: 56px;
    border: 2px solid var(--deep-red); padding-top: 5px;
    text-align: center; color: var(--brand-red); font-weight: 700;
  }
  .back-name .name-main { display: block; font-size: 25px; line-height: 26px; letter-spacing: -0.5px; }
  .back-name .name-sub { display: block; font-size: 10px; letter-spacing: 4.6px; margin-top: 4px; }
  .service-heading {
    position: absolute; right: 0; height: 24px; background: var(--ink);
    color: var(--white); font-weight: 700; font-size: 15px; letter-spacing: 1px;
    line-height: 24px; padding: 0 14px 0 14px; border: 2px solid #3c3232; border-right: none;
  }
  .heading-earthmoving { top: 107px; width: 143px; }
  .heading-transport { top: 208px; width: 128px; text-align: right; }
  .service-list { position: absolute; right: 14px; list-style: none; text-align: right;
    color: var(--white); font-size: 14.5px; line-height: 15px; letter-spacing: 0.4px; }
  .service-list li::after { content: ""; display: inline-block; width: 4px; height: 4px; border-radius: 50%;
    background: var(--ink); margin-left: 8px; vertical-align: middle; }
  .list-earthmoving { top: 138px; }
  .list-transport { top: 237px; }
</style>
</head>
<body>

<section class="card card-front">
  <div class="soil" role="img" aria-label="Close-up photograph of dark loose soil"></div>
  <h1 class="front-name"><span class="name-main">BK Harlowe</span><span class="name-sub">CONTRACTING</span></h1>

  <p class="contact contact-phone">0400 555 182
    <svg viewBox="0 0 24 24" aria-hidden="true"><path d="M6.6 10.8a15 15 0 0 0 6.6 6.6l2.2-2.2a1 1 0 0 1 1-.25 11.4 11.4 0 0 0 3.6.57 1 1 0 0 1 1 1V20a1 1 0 0 1-1 1A17 17 0 0 1 3 4a1 1 0 0 1 1-1h3.5a1 1 0 0 1 1 1c0 1.25.2 2.45.57 3.57a1 1 0 0 1-.25 1z"/></svg>
  </p>
  <p class="contact contact-address">42 Wattle Street, Dunmore 2830
    <svg viewBox="0 0 24 24" aria-hidden="true"><path d="M12 3 2 12h3v9h5v-6h4v6h5v-9h3z"/></svg>
  </p>
  <p class="contact contact-email">benharlowe@mailnet.com
    <svg viewBox="0 0 24 24" aria-hidden="true"><path d="M2 5h20v14H2z M3 6l9 7 9-7" /></svg>
  </p>

  <p class="tagline">Earthmoving &amp; Transport Solutions</p>
</section>

<section class="card card-back">
  <div class="back-soil" role="img" aria-label="Close-up photograph of dark loose soil"></div>
  <div class="divider"></div>
  <div class="machinery-photo" role="img" aria-label="Faint red-tinted photograph of a road grader at work"></div>
  <div class="truck-photo" role="img" aria-label="Photograph of a white prime mover truck"></div>

  <h2 class="back-name"><span class="name-main">BK Harlowe</span><span class="name-sub">CONTRACTING</span></h2>

  <h3 class="service-heading heading-earthmoving">EARTHMOVING</h3>
  <ul class="service-list list-earthmoving">
    <li>Road Building &amp; Maintenance</li>
    <li>Poly Pipe Laying</li>
    <li>Clearing fence lines</li>
    <li>Sand &amp; Gravel supplies</li>
  </ul>

  <h3 class="service-heading heading-transport">TRANSPORT</h3>
  <ul class="service-list list-transport">
    <li>Grain</li>
    <li>Cotton</li>
    <li>Sand &amp; Gravel</li>
    <li>Wool</li>
  </ul>
</section>

</body>
</html>
```